Komplette Präsentationsvorlage für Psychologen gewünscht
Zielgruppe
Ich bin Psychologe und trainiere in Seminaren Fach- und Führungskräften zu sozialen Kompetenzen.
Aufgabenstellung
Ich möchte eine PPT Vorlage / Folien-Master die folgende Kriterien erfüllt:
1. Passend zu meinem Corporate Design (Farben, Schriftarten, Logo) / Farbwerte #043D5D und #F15A29; Hintergrund überwiegend reinweiß und vereinzelt #D2D2D2
2. Folienmaster sollte folgendermaßen aufgebaut sein: oben rechts das Signet des Logos (Datei: Logo 546), unten rechts fortlaufende Seitenzahlen mit passendem Trenn-Symbol (*) in einer der beiden o.g. Farbwerte
3. Unten links das vollständige Logo in klein (Datei: Logo_2_346)
4. Vielfältige vorgestaltete Layout-Folien, die diverse Content-Darstellungen erlauben und in der Vorlage einprogrammiert sind (siehe unten)
Generell sollte sich das Gesamt-Design an der Vorlage eines Kunden orientieren, das für mich sehr passt. Ich lade zur Inspiration den betreffenden Folienmaster in den Dateien hoch.
Besonders wichtig ist mir Punkt 4 - in der benannten Inspirationsvorlage kann man diese reichhaltigen Layout-Folien gut einsehen durch Klick auf Einfügen > Neue Folien (das kleine Pfeil-Symbol). Vergleichbare Folien sollten bitte ebenfalls im Design gestaltet und genauso einprogrammiert sein, dass ich sie über Klick auf 'Neue Folien direkt auswählen kann. Der Schwerpunkt kann bei mir auf den Kategorien 'Titel und Inhalte', 'Text und Bild' liegen.
Weiterhin sollten auf den Folien ebenfalls verschiedene Grafiken / Piktogramme verfügbar sein, die einem gleichen Stil folgen (auch hier gefällt mir, der 'Comic/Skizzen' Stil meines Kunden sehr gut) - inhaltlich sollten die Grafiken vor allem soziale Situationen, Business-Themen, Verhandlungen, Speech, usw. betreffen. Gerne darf es auch eine Folie mit diversen Grafiken zur Auswahl als Sammlung geben.
(*) Ebenfalls in der Vorlage meines Kunden wird an diversen Stellen innerhalb der Präsentation ein abgerundeter roter 'Strich' verwendet, welcher auch als Trenn-Symbol für die Seitenzahl verwendet wird. Ich wünsche mir ein ähnlich durchgängig designt..

```html
<!DOCTYPE html>
<html lang="de">
<head>
<meta charset="utf-8">
<title>Präsentationsvorlage – Jonas Wendeborn</title>
<link href="https://fonts.googleapis.com/css2?family=Cinzel:wght@400;500&family=Roboto:wght@400;500&display=swap" rel="stylesheet">
<style>
:root{
  --navy:#043D5D;
  --orange:#F15A29;
  --grey:#D2D2D2;
  --light:#F0F0F0;
  --white:#FFFFFF;
  --board:#858585;
}
*{margin:0;padding:0;box-sizing:border-box}
html,body{width:1200px;height:1200px;overflow:hidden;background:var(--board)}
body{position:relative;font-family:'Roboto',sans-serif;color:var(--navy)}
.slide{position:absolute;width:346px;height:194px;background:var(--white);overflow:hidden}
.c1{left:53px}.c2{left:426px}.c3{left:799px}
.r1{top:61px}.r2{top:280px}.r3{top:499px}.r4{top:718px}.r5{top:937px}
.abs{position:absolute}
.serif{font-family:'Cinzel',serif}
.brand{position:absolute;display:flex;align-items:center;gap:4px}
.brand-dot{border-radius:50%;background:var(--orange);flex:none}
.brand-name{font-family:'Cinzel',serif;color:var(--navy);line-height:1;white-space:nowrap}
.brand-tag{font-family:'Cinzel',serif;color:var(--orange);line-height:1;white-space:nowrap}
.brand.lg .brand-dot{width:26px;height:26px}
.brand.lg .brand-name{font-size:15.5px}
.brand.lg .brand-tag{font-size:9px;margin-top:1px}
.brand.sm{left:9px;bottom:8px}
.brand.sm .brand-dot{width:12px;height:12px}
.brand.sm .brand-name{font-size:8px}
.brand.sm .brand-tag{font-size:4.6px}
.signet{position:absolute;top:12px;right:12px;width:22px;height:22px;border-radius:50%;background:var(--orange)}
.page{position:absolute;right:11px;bottom:8px;font-family:'Cinzel',serif;font-size:7.5px;color:var(--navy);display:flex;align-items:center;gap:3px}
.page::before{content:"";width:5px;height:5px;border-radius:50%;background:var(--orange)}
.pill{position:absolute;left:0;top:10px;height:25px;border-radius:0 13px 13px 0;padding:0 14px 0 20px;color:var(--white);font-family:'Cinzel',serif;display:flex;flex-direction:column;justify-content:center;line-height:1.1}
.pill .main{font-size:8.4px}
.pill .sub{font-size:5px}
.pill::after{content:"";position:absolute;left:18px;bottom:-5px;border:4px solid transparent}
.pill.navy{background:var(--navy)}
.pill.orange{background:var(--orange)}
.pill.navy::after{border-top-color:var(--navy)}
.pill.orange::after{border-top-color:var(--orange)}
.title-pill{position:absolute;left:0;height:23px;border-radius:0 12px 12px 0;color:var(--white);font-family:'Cinzel',serif;font-size:13.5px;display:flex;align-items:center;padding-left:22px}
.title-pill::after{content:"";position:absolute;left:20px;bottom:-5px;border:4px solid transparent}
.title-pill.orange{background:var(--orange)}.title-pill.orange::after{border-top-color:var(--orange)}
.title-pill.navy{background:var(--navy)}.title-pill.navy::after{border-top-color:var(--navy)}
.kicker{font-family:'Cinzel',serif;font-size:6.8px}
.topic{font-size:10.5px;line-height:1.15}
.date{font-family:'Cinzel',serif;font-size:5.8px;display:flex;align-items:center;gap:2px}
.date::before{content:"";border:2.5px solid transparent;border-left:3.5px solid var(--orange)}
.bullets{list-style:none;font-size:7.6px;line-height:1.42}
.bullets li{position:relative;padding-left:9px}
.bullets li::before{content:"";position:absolute;left:0;top:2.5px;border:2.5px solid transparent;border-left:3.5px solid var(--orange)}
.bullets.white{color:var(--white)}
.bullets.white li::before{border-left-color:var(--white)}
.bullets.small{font-size:5.2px;line-height:1.35}
.bullets.small li{margin-bottom:8px;padding-left:6px}
.bullets.small li::before{top:1px;border-width:2px;border-left-width:3px}
.para{font-size:5px;line-height:1.35}
.para p+p{margin-top:6px}
.art{position:absolute}
.panel-grey{position:absolute;background:var(--light)}
.chip{background:var(--navy);color:var(--white);font-size:5.6px;border-radius:6px;padding:2px 9px;text-align:center}
.card{flex:1;height:112px;background:var(--light);border-radius:6px}
.card .photo{margin:2px;height:60px;border-radius:5px}
.card .label{margin:2px;height:14px;border-radius:7px;background:var(--orange);color:var(--white);font-size:7px;display:flex;align-items:center;justify-content:center}
</style>
</head>
<body>

<section class="slide c1 r1">
  <div class="brand lg" style="left:25px;top:14px"><span class="brand-dot"></span><div><div class="brand-name">JONAS WENDEBORN</div><div class="brand-tag">TRAINING • BERATUNG • COACHING</div></div></div>
  <div class="title-pill orange" style="top:78px;width:154px">PRÄSENTATION</div>
  <div class="abs kicker" style="left:23px;top:113px">THEMATISCH:</div>
  <div class="abs topic" style="left:23px;top:120px">Lorem ipsumdolor Dolore</div>
  <div class="abs date" style="left:23px;top:168px">MITTWOCH, 6. DEZEMBER 2023</div>
  <div class="art" role="img" aria-label="Illustration: Team am Besprechungstisch vor einer Präsentationstafel mit Diagrammen" style="left:160px;top:48px;width:175px;height:128px;border-radius:40px;background:linear-gradient(135deg,#EDEDED,#D9EEF0)"></div>
</section>

<section class="slide c2 r1" style="background:var(--light)">
  <div class="abs" style="left:0;top:0;width:346px;height:55px;background:var(--white);border-radius:0 0 14px 14px"></div>
  <div class="brand lg" style="left:61px;top:14px"><span class="brand-dot"></span><div><div class="brand-name">JONAS WENDEBORN</div><div class="brand-tag">TRAINING • BERATUNG • COACHING</div></div></div>
  <div class="title-pill navy" style="top:91px;width:154px">PRÄSENTATION</div>
  <div class="abs kicker" style="left:23px;top:127px">THEMATISCH:</div>
  <div class="abs topic" style="left:23px;top:134px">Lorem ipsumdolor Dolore</div>
  <div class="art" role="img" aria-label="Illustration: Referent vor einem Flipchart mit Diagrammen" style="left:172px;top:62px;width:168px;height:115px;border-radius:40px 40px 0 0;background:linear-gradient(135deg,#E0E0E0,#CFEFF2)"></div>
  <div class="abs" style="left:0;top:175px;width:346px;height:19px;background:var(--orange);border-radius:14px 14px 0 0"></div>
  <div class="abs date" style="left:23px;top:182px;color:var(--white)">MITTWOCH, 6. DEZEMBER 2023</div>
</section>

<section class="slide c3 r1">
  <div class="brand lg" style="left:61px;top:14px"><span class="brand-dot"></span><div><div class="brand-name">JONAS WENDEBORN</div><div class="brand-tag">TRAINING • BERATUNG • COACHING</div></div></div>
  <div class="abs" style="left:0;top:55px;width:346px;height:117px;background:var(--light)"></div>
  <div class="abs" style="left:0;top:55px;width:181px;height:117px;background:var(--navy);border-radius:0 14px 14px 0"></div>
  <div class="title-pill orange" style="top:82px;width:156px">PRÄSENTATION</div>
  <div class="abs kicker" style="left:26px;top:117px;color:var(--white)">THEMATISCH:</div>
  <div class="abs topic" style="left:26px;top:124px;color:var(--white)">Lorem ipsum dolor<br>Consectetuer adipiscing</div>
  <div class="art" role="img" aria-label="Illustration: Seminarraum mit Referent und Teilnehmenden" style="left:192px;top:62px;width:145px;height:104px;border-radius:30px;background:linear-gradient(135deg,#DADADA,#F3E4DC)"></div>
  <div class="abs date" style="left:26px;top:180px">MITTWOCH, 6. DEZEMBER 2023</div>
</section>

<section class="slide c1 r2">
  <div class="pill navy" style="width:185px"><span class="main">AGENDA FÜR DIE HEUTIGE SESSION</span></div>
  <div class="signet"></div>
  <div class="panel-grey" style="left:0;top:47px;width:346px;height:118px"></div>
  <ul class="bullets abs" style="left:23px;top:63px">
    <li>Lorem ipsum dolor</li><li>Consectetuer adipiscing</li><li>Elitsed diam nonummy nibh</li><li>Dolore magna aliquam erat</li><li>Veniam, quis nostrud</li><li>Exerci tation ullamcorper</li><li>Suscipit lobortis nisl ut</li><li>Aliquip ex ea com</li>
  </ul>
  <div class="abs" style="left:244px;top:47px;width:102px;height:118px;background:var(--orange);border-radius:14px 0 0 14px"></div>
  <div class="art" role="img" aria-label="Illustration: zwei Personen im Gespräch am Tisch mit Sprechblasen" style="left:160px;top:40px;width:130px;height:120px;border-radius:30px;background:linear-gradient(135deg,#CFEFF2,#F7D0C2)"></div>
  <div class="brand sm"><span class="brand-dot"></span><div><div class="brand-name">JONAS WENDEBORN</div><div class="brand-tag">TRAINING • BERATUNG • COACHING</div></div></div>
  <div class="page">02</div>
</section>

<section class="slide c2 r2">
  <div class="pill navy" style="width:185px"><span class="main">LOREM IPSUM DOLOR ADIPISCING</span></div>
  <div class="signet"></div>
  <div class="art" role="img" aria-label="Illustration: Gruppe diskutierender Menschen mit Sprechblasen" style="left:18px;top:55px;width:150px;height:100px;border-radius:40px;background:linear-gradient(135deg,#CFEFF2,#F7D8CC)"></div>
  <div class="abs" style="left:190px;top:46px;width:156px;height:124px;background:var(--orange);border-radius:12px 0 0 12px"></div>
  <ul class="bullets white abs" style="left:206px;top:60px">
    <li>Lorem ipsum dolor</li><li>Consectetuer adipiscing</li><li>Elitsed diam nonummy nibh</li><li>Dolore magna aliquam erat</li><li>Veniam, quis nostrud</li><li>Exerci tation ullamcorper</li><li>Suscipit lobortis nisl ut</li><li>Aliquip ex ea com</li>
  </ul>
  <div class="brand sm"><span class="brand-dot"></span><div><div class="brand-name">JONAS WENDEBORN</div><div class="brand-tag">TRAINING • BERATUNG • COACHING</div></div></div>
  <div class="page">00</div>
</section>

<section class="slide c3 r2">
  <div class="pill navy" style="width:127px"><span class="main">SBSH-FAKTOREN</span><span class="sub">NACH PROF. ERIK HALDEN</span></div>
  <div class="signet"></div>
  <div class="abs" style="left:32px;top:50px;width:290px;display:flex;gap:6px">
    <div class="card"><div class="photo" role="img" aria-label="Foto: Familie sitzt geborgen zusammen" style="background:linear-gradient(135deg,#C9B8A8,#E9E1D8)"></div><div class="label">Sicherheit</div></div>
    <div class="card"><div class="photo" role="img" aria-label="Foto: Hände vieler Menschen übereinander" style="background:linear-gradient(135deg,#6E5A4E,#B8A090)"></div><div class="label">Bindung</div></div>
    <div class="card"><div class="photo" role="img" aria-label="Foto: Frau lächelt in einen Spiegel" style="background:linear-gradient(135deg,#D8C8B8,#F2ECE4)"></div><div class="label">Selbstwert</div></div>
    <div class="card"><div class="photo" role="img" aria-label="Foto: feiernde Menschen mit Konfetti" style="background:linear-gradient(135deg,#B89A8A,#EAD6CF)"></div><div class="label">Hedonismus</div></div>
  </div>
  <svg class="abs" style="left:55px;top:131px" width="240" height="24" viewBox="0 0 240 24">
    <path d="M0 12 L14 2 L14 22 Z" fill="#043D5D"/>
    <line x1="22" y1="12" x2="218" y2="12" stroke="#043D5D" stroke-width="2" stroke-dasharray="1.5 3.5" stroke-linecap="round"/>
    <path d="M240 12 L226 2 L226 22 Z" fill="#043D5D"/>
  </svg>
  <div class="brand sm"><span class="brand-dot"></span><div><div class="brand-name">JONAS WENDEBORN</div><div class="brand-tag">TRAINING • BERATUNG • COACHING</div></div></div>
  <div class="page">08</div>
</section>

<section class="slide c1 r3">
  <div class="abs" style="left:0;top:25px;width:294px;height:139px;background:var(--navy);border-radius:0 14px 14px 0"></div>
  <div class="pill orange" style="width:194px"><span class="main">GEMEINSAMER EINSTIEG IN DEN TAG</span><span class="sub">CHECK-IN</span></div>
  <div class="signet"></div>
  <div class="abs" style="left:23px;top:77px;color:var(--white);font-size:9px;font-weight:500;display:flex;align-items:center;gap:4px"><span style="border:3px solid transparent;border-left:4px solid var(--orange)"></span>1 prägnanter Satz:</div>
  <div class="abs" style="left:23px;top:99px;color:var(--white);font-size:7.6px;line-height:1.4;width:136px">Worauf freue ich mich heute am meisten, bzw. was interessiert mich besonders zu diesem Thema?</div>
  <div class="art" role="img" aria-label="Illustration: jubelnd springende Person" style="left:180px;top:42px;width:125px;height:135px;border-radius:30px;background:linear-gradient(160deg,#CFEFF2,#F5C1AC)"></div>
  <div class="brand sm"><span class="brand-dot"></span><div><div class="brand-name">JONAS WENDEBORN</div><div class="brand-tag">TRAINING • BERATUNG • COACHING</div></div></div>
  <div class="page">03</div>
</section>

<section class="slide c2 r3">
  <div class="panel-grey" style="left:0;top:0;width:346px;height:165px;border-radius:0 0 14px 14px"></div>
  <div class="pill orange" style="width:194px"><span class="main">LOREM IPSUM DOLOR ADIPISCING</span><span class="sub">LOREM IPSUM</span></div>
  <div class="signet"></div>
  <svg class="abs" style="left:20px;top:55px" width="6" height="92" viewBox="0 0 6 92"><path d="M3 0 L6 4 L0 4 Z M0 88 L6 88 L3 92 Z" fill="#043D5D"/><line x1="3" y1="6" x2="3" y2="86" stroke="#043D5D" stroke-width=".6"/></svg>
  <ul class="abs" style="left:36px;top:60px;list-style:none;font-size:7.6px;line-height:1.42">
    <li>Lorem ipsum dolor</li><li>Consectetuer adipiscing</li><li>Elitsed diam nonummy nibh</li><li>Dolore magna aliquam erat</li><li>Veniam, quis nostrud</li><li>Exerci tation ullamcorper</li><li>Suscipit lobortis nisl ut</li><li>Aliquip ex ea com</li>
  </ul>
  <div class="art" role="img" aria-label="Illustration: Kopf im Profil mit Zahnrädern und kleinen Figuren" style="left:168px;top:42px;width:170px;height:110px;border-radius:40px;background:linear-gradient(135deg,#E0E0E0,#CFEFF2)"></div>
  <div class="brand sm"><span class="brand-dot"></span><div><div class="brand-name">JONAS WENDEBORN</div><div class="brand-tag">TRAINING • BERATUNG • COACHING</div></div></div>
  <div class="page">00</div>
</section>

<section class="slide c3 r3">
  <div class="pill orange" style="width:194px"><span class="main">KÖRPERSPRACHE &amp; PRÄSENZ</span><span class="sub">WAHRNEHMUNGSKATEGORIEN: ALLES SPRICHT</span></div>
  <div class="signet"></div>
  <div class="art" role="img" aria-label="Illustration: stehender Mann mit verschränkten Armen" style="left:40px;top:48px;width:60px;height:118px;border-radius:30px;background:linear-gradient(180deg,#D8D8D8,#F4B79F)"></div>
  <div class="abs" style="left:100px;top:48px;width:100px;border-top:0.6px dotted #999"></div>
  <div class="abs" style="left:106px;top:54px;display:flex;flex-direction:column;gap:7px">
    <div class="chip">Kopf &amp; Mimik</div>
    <div class="chip">Arme &amp; Brust</div>
    <div class="chip" style="padding:2px 5px">Ventrum, Bauch</div>
    <div class="chip" style="margin-top:24px">Beine &amp; Füsse</div>
  </div>
  <svg class="abs" style="left:198px;top:44px" width="126" height="126" viewBox="0 0 126 126">
    <g font-family="Roboto, sans-serif" font-size="10" fill="#fff">
      <path d="M3 58 A60 60 0 0 1 58 3 L58 33 A30 30 0 0 0 33 58 Z" fill="#043D5D"/>
      <path d="M68 3 A60 60 0 0 1 123 58 L93 58 A30 30 0 0 0 68 33 Z" fill="#1A5A72"/>
      <path d="M3 68 A60 60 0 0 0 58 123 L58 93 A30 30 0 0 1 33 68 Z" fill="#1F6E80"/>
      <path d="M123 68 A60 60 0 0 1 68 123 L68 93 A30 30 0 0 0 93 68 Z" fill="#155F76"/>
      <text x="18" y="42" transform="rotate(-45 30 35)">Mimik</text>
      <text x="78" y="30" transform="rotate(45 90 35)">Gestik</text>
      <text x="16" y="95" transform="rotate(45 30 92)">Proxemik</text>
      <text x="80" y="105" transform="rotate(-45 92 92)">Motorik</text>
    </g>
  </svg>
  <div class="brand sm"><span class="brand-dot"></span><div><div class="brand-name">JONAS WENDEBORN</div><div class="brand-tag">TRAINING • BERATUNG • COACHING</div></div></div>
  <div class="page">09</div>
</section>

<section class="slide c1 r4">
  <div class="panel-grey" style="left:0;top:0;width:346px;height:164px;border-radius:0 0 14px 14px"></div>
  <div class="pill navy" style="width:194px"><span class="main">MEINE EINSTELLUNGEN ZUM THEMA</span><span class="sub">INTERVIEWS</span></div>
  <div class="signet"></div>
  <div class="art" role="img" aria-label="Illustration: nachdenkliche Person auf einem großen Fragezeichen" style="left:18px;top:46px;width:85px;height:110px;border-radius:30px;background:linear-gradient(160deg,#BFEAEE,#F5C1AC)"></div>
  <ul class="bullets small abs" style="left:120px;top:61px;width:212px">
    <li>Welche Erfahrungen hast du gemacht zum Thema öffentliche Wirksamkeit, Sicht- und Hörbarkeit?</li>
    <li>Was glaubst du über dich selbst, in solchen Situationen?</li>
    <li>Was denkst du, glauben die anderen über dich?</li>
    <li>Was hast du diesbezüglich vorgelebt bekommen, von Modellen, Eltern, etc.?</li>
    <li>Was gelingt dir leicht? Was schwer? Was möchtest du gerne verändern?</li>
  </ul>
  <div class="brand sm"><span class="brand-dot"></span><div><div class="brand-name">JONAS WENDEBORN</div><div class="brand-tag">TRAINING • BERATUNG • COACHING</div></div></div>
  <div class="page">04</div>
</section>

<section class="slide c2 r4">
  <div class="panel-grey" style="left:0;top:0;width:346px;height:164px;border-radius:0 0 14px 14px"></div>
  <div class="pill navy" style="width:194px"><span class="main">LOREM IPSUM DOLOR ADIPISCING</span><span class="sub">LOREM IPSUM</span></div>
  <div class="signet"></div>
  <div class="art" role="img" aria-label="Illustration: Menschen im Gespräch mit Sprechblasen" style="left:14px;top:50px;width:180px;height:114px;border-radius:30px 30px 0 0;background:linear-gradient(135deg,#FFFFFF,#CFEFF2)"></div>
  <div class="para abs" style="left:211px;top:52px;width:120px">
    <p>Lorem ipsum dolor sit amet, consectetur adipiscing elit. Curabitur posuere pulvinar odio at maximus. Curabitur facilisis risus id mollis finibus. Nullam ac eleifend nibh. Pellentesque interdum facilisis massa id luctus.</p>
    <p>Fusce quis maximus nisi, quis tempus est. Vestibulum erat arcu, vulputate in lacinia id, interdum feugiat enim. Class aptent taciti sociosqu ad litora torquent per conubia nostra, per inceptos himenaeos.</p>
  </div>
  <div class="brand sm"><span class="brand-dot"></span><div><div class="brand-name">JONAS WENDEBORN</div><div class="brand-tag">TRAINING • BERATUNG • COACHING</div></div></div>
  <div class="page">00</div>
</section>

<section class="slide c3 r4">
  <div class="panel-grey" style="left:0;top:28px;width:346px;height:136px;border-radius:14px 0 14px 14px"></div>
  <div class="pill navy" style="width:117px"><span class="main">STIMM-MUSTER</span><span class="sub">ERGOTROP</span></div>
  <div class="signet"></div>
  <ul class="bullets small abs" style="left:22px;top:63px;width:140px">
    <li>Deutliche Rhythmen</li>
    <li>Akzentuierung</li>
    <li>Beschleunigung im Sprechtempo</li>
    <li>Große Dynamikunterschiede in der Lautstärke</li>
    <li>Starker Auftrieb und Abfall der Tonmelodien, starke Tonhöhenunterschiede</li>
  </ul>
  <div class="abs" style="left:207px;top:38px;width:78px;height:78px;border-radius:50%;background:var(--orange);border:3px solid #F7A98D;color:var(--white);font-size:7.8px;line-height:1.2;display:flex;flex-direction:column;align-items:center;justify-content:center;text-align:center"><span style="font-weight:500">Ziel:</span><span>Aktivierung und Informations-<br>aufnahme</span></div>
  <div class="art" role="img" aria-label="Grafik: Stimm-Wellenform mit starken Ausschlägen" style="left:169px;top:121px;width:154px;height:34px;border-radius:8px;background:linear-gradient(90deg,#C8C8C8,#D2D2D2)"></div>
  <div class="brand sm"><span class="brand-dot"></span><div><div class="brand-name">JONAS WENDEBORN</div><div class="brand-tag">TRAINING • BERATUNG • COACHING</div></div></div>
  <div class="page">10</div>
</section>

<section class="slide c1 r5">
  <div class="panel-grey" style="left:0;top:30px;width:257px;height:133px;border-radius:0 14px 14px 0"></div>
  <div class="signet"></div>
  <div class="art" role="img" aria-label="Illustration: Kaffeetasse von oben mit langem Schatten" style="left:20px;top:42px;width:120px;height:110px;border-radius:50%;background:linear-gradient(135deg,#F47A50,#E8531F)"></div>
  <div class="abs serif" style="left:168px;top:80px;height:23px;width:165px;background:var(--orange);border-radius:12px;color:var(--white);font-size:13.5px;display:flex;align-items:center;justify-content:center">EINE KURZE PAUSE...</div>
  <div class="abs serif" style="left:186px;top:110px;font-size:9px">VIEL SPASS!</div>
  <div class="brand sm"><span class="brand-dot"></span><div><div class="brand-name">JONAS WENDEBORN</div><div class="brand-tag">TRAINING • BERATUNG • COACHING</div></div></div>
  <div class="page">05</div>
</section>

<section class="slide c2 r5">
  <div class="panel-grey" style="left:0;top:0;width:346px;height:164px;border-radius:0 0 14px 14px"></div>
  <div class="pill orange" style="width:194px"><span class="main">LOREM IPSUM DOLOR ADIPISCING</span><span class="sub">LOREM IPSUM</span></div>
  <div class="signet"></div>
  <div class="para abs" style="left:22px;top:53px;width:120px">
    <p>Lorem ipsum dolor sit amet, consectetur adipiscing elit. Curabitur posuere pulvinar odio at maximus. Curabitur facilisis risus id mollis finibus. Nullam ac eleifend nibh. Pellentesque interdum facilisis massa id luctus.</p>
    <p>Fusce quis maximus nisi, quis tempus est. Vestibulum erat arcu, vulputate in lacinia id, interdum feugiat enim. Class aptent taciti sociosqu ad litora torquent per conubia nostra, per inceptos himenaeos.</p>
  </div>
  <div class="art" role="img" aria-label="Illustration: nachdenkende Person im Schneidersitz mit Glühbirne und Pflanzen" style="left:178px;top:38px;width:160px;height:122px;border-radius:40px;background:linear-gradient(135deg,#CFEFF2,#F5C1AC)"></div>
  <div class="brand sm"><span class="brand-dot"></span><div><div class="brand-name">JONAS WENDEBORN</div><div class="brand-tag">TRAINING • BERATUNG • COACHING</div></div></div>
  <div class="page">04</div>
</section>

<section class="slide c3 r5">
  <div class="abs serif" style="left:26px;top:46px;width:294px;height:59px;background:var(--navy);border-radius:30px;color:var(--white);font-size:13px;display:flex;align-items:center;justify-content:center">DANKE FÜR IHRE AUFMERKSAMKEIT...</div>
  <div class="brand lg" style="left:81px;top:128px"><span class="brand-dot"></span><div><div class="brand-name">JONAS WENDEBORN</div><div class="brand-tag">TRAINING • BERATUNG • COACHING</div></div></div>
</section>

</body>
</html>
```